Buch-/E-Book-Cover für Sachbuch über Hunderasse
Zielgruppe
Ich benötige ein Buch-Cover im DIN A5 Format für ein anspruchsvolles Sachbuch, das die rassetypischen Krankheiten der Hunderasse Rhodesian Ridgeback thematisiert. Die Zielgruppe sind Züchter, Tierärzte und Liebhaber der Rasse.
Aufgabenstellung
Den größten Raum sollte ein Foto der Rasse einnehmen. Das Foto würde ich stellen, im Entwurf kann also ein Beispielfoto verwendet werden. Da das Buch der Auftakt zu einer Reihe ist, sollte das Design einen hohen Wiedererkennungswert haben und in erster Linie seriös wirken. Das Foto, der Rassename und die verwendeten Farben sollten leicht austauschbar sein. Sowohl der Titel als auch der Untertitel sind recht lang. Der Arbeitstitel lautet: Stille Pfade im Nebel der Ostseeküste, Untertitel: Geschichten von Fischern und Leuchttürmen.

```html
<!DOCTYPE html>
<html lang="de">
<head>
<meta charset="utf-8">
<title>Stille Pfade im Nebel der Ostseeküste – Cover</title>
<link rel="stylesheet" href="https://fonts.googleapis.com/css2?family=Jost:wght@400&family=Archivo:wght@700&display=swap">
<style>
  :root {
    --page-bg: #ffffff;
    --rust: #c9602f;
    --rust-deep: #b04f24;
    --rust-light: #d6733f;
    --lavender: #b69ad0;
    --lavender-light: #d9b9df;
    --lavender-mid: #a98cc8;
    --photo-warm: #b2642f;
    --ink: #111111;
    --box: #050505;
    --box-text: #d9c6ea;
    --white: #ffffff;
  }
  * { margin: 0; padding: 0; box-sizing: border-box; }
  html, body {
    width: 1200px; height: 800px; overflow: hidden;
    background: var(--page-bg);
  }
  .canvas {
    position: relative; width: 1200px; height: 800px;
    display: flex; align-items: center; justify-content: center;
  }
  .cover {
    position: relative; width: 520px; height: 736px; overflow: hidden;
    background: var(--lavender-light);
    box-shadow: 0 10px 30px rgba(0,0,0,0.18);
  }
  .cover-photo {
    position: absolute; left: 0; top: 265px; width: 100%; height: 471px;
    background:
      radial-gradient(ellipse 38% 55% at 45% 62%, var(--photo-warm) 0%, var(--photo-warm) 55%, rgba(178,100,47,0) 75%),
      linear-gradient(160deg, var(--lavender-light) 0%, var(--lavender-mid) 60%, var(--lavender) 100%);
  }
  .accent-strip {
    position: absolute; top: 12px; right: 45px; width: 52px; height: 660px;
    background: var(--lavender);
  }
  .title-band {
    position: absolute; left: 0; top: 0; width: 437px; height: 265px;
    background: linear-gradient(135deg, var(--rust-light) 0%, var(--rust) 55%, var(--rust-deep) 100%);
  }
  .title {
    position: absolute; left: 38px; top: 38px;
    font-family: "Jost", "Futura", sans-serif; font-weight: 400;
    font-size: 66px; line-height: 0.88; letter-spacing: -1px;
    color: var(--ink); text-transform: uppercase;
  }
  .title span { display: block; }
  .subtitle {
    position: absolute; left: 40px; top: 226px;
    font-family: "Jost", "Futura", sans-serif; font-weight: 400;
    font-size: 15px; letter-spacing: 2.4px; color: var(--white);
    text-transform: uppercase;
  }
  .tagline-box {
    position: absolute; left: 76px; top: 575px; width: 422px; height: 122px;
    background: var(--box);
    display: flex; align-items: center; padding-left: 32px;
  }
  .tagline {
    font-family: "Archivo", "Arial", sans-serif; font-weight: 700;
    font-size: 19px; line-height: 1.35; color: var(--box-text);
    text-transform: uppercase; letter-spacing: 0.2px;
  }
</style>
</head>
<body>
  <div class="canvas">
    <article class="cover">
      <div class="cover-photo" role="img" aria-label="Porträtfoto eines rotbraunen Hundes im Profil vor lavendelfarbenem Hintergrund"></div>
      <div class="accent-strip"></div>
      <header class="title-band" role="img" aria-label="Nahaufnahme eines Hundeauges in rostbraunem Farbton">
        <h1 class="title"><span>Stille</span><span>Pfade im</span><span>Nebel</span></h1>
        <p class="subtitle">der Ostseeküste</p>
      </header>
      <div class="tagline-box">
        <p class="tagline">Geschichten von Fischern<br>und Leuchttürmen</p>
      </div>
    </article>
  </div>
</body>
</html>
```